ReDesign Website for a more Bold approach

Hello! I'd like to redesign my website: holvencrest.com

I'd like to add one thing that's not on my website which is a blog. The design around the blog should be put time into as I will be putting out incredibly great content and want it to attract viewers.

I get a lot of inspiration from ruvtal.com (the way they flow the big statements across each screen, colors)
moorlane.vc (the simplicity behind the design is beautiful)

I like modern very simple but bold approaches.

I am going to attach my logo here and if it can be thought of when making the design of the website. Thanks!

Industry/Entity Type

Finance and Private Equity

Number of Pages Required

3 page

Font styles to use
Serif
Sans Serif

Colors
0054AA
0677BA
7BADD7
CADEEF
E8F1F8
0094D4
00A9DD
6FCCEA
C7EBF8
E9F6FB
00AB8E
00BBA5
67D7C9
C6EFE9
E9F9F6

Requirements
Must have
• My project must have a Home, Expertise, Story, Clients, Approach, Blog, Contact
Nice to have
• It would be nice to have these tabs reduced to 1-3 pages
Should not have
• My project must not have bright colors.

```html
<!DOCTYPE html>
<html lang="en">
<head>
<meta charset="utf-8">
<title>Holvencrest Ventures — Blog</title>
<link href="https://fonts.googleapis.com/css2?family=Crimson+Pro:wght@400;600;700&family=Karla:wght@400;600;700&display=swap" rel="stylesheet">
<style>
  :root {
    --navy: #13294b;
    --hero-bg: #e6eef7;
    --teal: #00ab8e;
    --text: #3a3f45;
    --muted: #6b7078;
    --rule: #e3e6ea;
    --dark: #2b2b2b;
    --footer-bg: #243447;
    --footer-text: #ffffff;
    --link: #5a7fb8;
    --white: #ffffff;
  }
  * { box-sizing: border-box; margin: 0; padding: 0; }
  html, body { width: 1200px; height: 4102px; overflow: hidden; }
  body { position: relative; background: var(--white); font-family: "Karla", sans-serif; color: var(--text); }

  .site-header { position: absolute; left: 0; top: 0; width: 1200px; height: 339px; background: var(--hero-bg); }
  .brand { position: absolute; left: 75px; top: 18px; font-weight: 700; color: var(--navy); font-size: 32px; letter-spacing: 1px; line-height: 38px; }
  .brand .sub, .footer-brand .sub { display: block; font-size: 19px; letter-spacing: 8px; line-height: 24px; margin-left: 8px; font-weight: 400; }
  .main-nav a { position: absolute; top: 38px; font-size: 13px; font-weight: 600; color: var(--navy); text-decoration: none; letter-spacing: .5px; }
  .header-rule { position: absolute; left: 67px; top: 95px; width: 1066px; height: 1px; background: #d3dde9; }
  .hero-title { position: absolute; left: 127px; top: 145px; font-family: "Crimson Pro", serif; font-weight: 700; font-size: 56px; color: var(--navy); line-height: 64px; isolation: isolate; }
  .hero-title .accent { position: relative; display: inline-block; }
  .hero-title .accent::after { content: ""; position: absolute; left: 0; right: -6px; bottom: 6px; height: 14px; background: var(--teal); border-radius: 7px; z-index: 0; }
  .hero-title .accent span { position: relative; z-index: 1; }
  .hero-sub { position: absolute; left: 127px; top: 224px; font-size: 21px; color: var(--navy); }

  .post-list { position: absolute; left: 127px; top: 389px; width: 611px; }
  .post { padding: 38px 0 43px; border-bottom: 1px solid var(--rule); }
  .post:last-child { border-bottom: none; }
  .post-title { max-width: 590px; font-family: "Crimson Pro", serif; font-weight: 600; font-size: 41px; line-height: 45px; color: #2f3238; letter-spacing: .4px; }
  .post-title.compact { font-size: 35px; }
  .post-date { margin-top: 12px; font-size: 13px; font-weight: 700; line-height: 16px; letter-spacing: .6px; color: #3a3f45; }
  .post-image { margin-top: 29px; width: 611px; height: 298px; }
  .post-excerpt { margin-top: 13px; width: 600px; font-size: 16.5px; line-height: 30px; color: var(--muted); }
  .post-excerpt a { color: var(--link); }
  .read-more { display: inline-block; margin-top: 18px; font-size: 15px; font-weight: 700; line-height: 20px; letter-spacing: .8px; color: #2f3238; text-decoration: none; }

  .sidebar { position: absolute; left: 820px; top: 424px; width: 251px; }
  .widget-title { font-family: "Crimson Pro", serif; font-weight: 400; font-size: 17px; letter-spacing: 1px; color: #2f3238; }
  .search-input { display: block; margin-top: 18px; width: 251px; height: 43px; border: 1px solid #cfd3d8; background: var(--white); }
  .search-submit { display: block; margin: 14px 0 0 159px; width: 92px; height: 37px; background: var(--dark); color: var(--white); border: none; font-family: "Karla", sans-serif; font-weight: 700; font-size: 12px; letter-spacing: .6px; }
  .widget-rule { margin-top: 32px; height: 1px; background: var(--rule); }
  .latest { margin-top: 25px; }
  .latest ul { list-style: none; margin-top: 14px; }
  .latest li { font-family: "Crimson Pro", serif; font-weight: 400; font-size: 15px; line-height: 24px; color: var(--navy); margin-bottom: 22px; }

  .pager { position: absolute; top: 3702px; width: 157px; height: 34px; background: var(--dark); color: var(--white); font-size: 12px; font-weight: 700; letter-spacing: .4px; text-decoration: none; display: flex; align-items: center; justify-content: center; gap: 10px; }
  .pager.older { left: 129px; }
  .pager.newer { left: 610px; }

  .site-footer { position: absolute; left: 0; top: 3828px; width: 1200px; height: 274px; background: var(--footer-bg); color: var(--footer-text); }
  .footer-brand { position: absolute; left: 67px; top: 70px; font-weight: 700; font-size: 32px; line-height: 38px; letter-spacing: 1px; }
  .footer-nav a { position: absolute; top: 89px; font-size: 14px; font-weight: 700; color: var(--footer-text); text-decoration: none; letter-spacing: .5px; }
  .social { position: absolute; top: 74px; width: 46px; height: 47px; background: #dfe6ee; border-radius: 5px; }
  .footer-rule { position: absolute; left: 67px; top: 212px; width: 1066px; height: 1px; background: #3e4f63; }
  .copyright { position: absolute; left: 67px; top: 235px; font-size: 13px; color: #c9d1da; }
  .legal { position: absolute; right: 67px; top: 235px; font-size: 13px; color: #c9d1da; }
  .legal a { color: #7fb0e0; }
</style>
</head>
<body>

<header class="site-header">
  <div class="brand">HOLVENCREST<span class="sub">VENTURES</span></div>
  <nav class="main-nav">
    <a href="#" style="left:839px">HOME</a>
    <a href="#" style="left:953px">BLOG</a>
    <a href="#" style="left:1061px">CONTACT</a>
  </nav>
  <div class="header-rule"></div>
  <h1 class="hero-title">Welcome To Our <span class="accent"><span>Blog</span></span></h1>
  <p class="hero-sub">The Latest on Starting and Growing a Business</p>
</header>

<main class="post-list">
  <article class="post">
    <h2 class="post-title">How to build a growth team – lessons from Ridewell, Salesloom, and others</h2>
    <p class="post-date">FEBRUARY 10, 2022</p>
    <div class="post-image" role="img" aria-label="Typewriter with a sheet reading venture capital" style="background:linear-gradient(180deg,#1a1a1a 0%,#cfd2d4 40%,#56635c 75%,#2e3431 100%)"></div>
    <p class="post-excerpt">The typical venture capital investment occurs after an initial "seed funding" round. The first round of <a href="#">institutional venture capital</a> to fund growth is called the Series A round.  via a sale to another entity such as a financial buyer in the private equity secondary market or via a sale to a trading company such as a competitor [ . . . ]</p>
    <a class="read-more" href="#">READ MORE &nbsp;&gt;</a>
  </article>

  <article class="post">
    <h2 class="post-title">3 Ways You Can Reinvent Funding round&nbsp; Without Looking Like An Amateur</h2>
    <p class="post-date">FEBRUARY 10, 2022</p>
    <div class="post-image" role="img" aria-label="Printed stock chart with a green line" style="background:linear-gradient(160deg,#f4f5f5 0%,#e9ecea 60%,#9aa3a0 85%,#3a3f3d 100%)"></div>
    <p class="post-excerpt">The private-equity fund, still in use today, emerged. Private-equity firms organized limited partnerships to hold investments in which the investment professionals served as limited general partner and the investors, limited who were passive limited partners, put up the capital. [ . . . ]</p>
    <a class="read-more" href="#">READ MORE &nbsp;&gt;</a>
  </article>

  <article class="post">
    <h2 class="post-title">Top 10 Tips To Grow Your Business In 1 Year</h2>
    <p class="post-date">FEBRUARY 10, 2022</p>
    <div class="post-image" role="img" aria-label="Light typewriter with a sheet reading startup investments" style="background:linear-gradient(180deg,#ece7df 0%,#e6e8e6 45%,#c9cfcb 70%,#5b6260 100%)"></div>
    <p class="post-excerpt">Innovator supply chain partner network scrum project pivot monetization chirply business-to-consumer metrics feedloop low hanging fruit. party traction. Buyer customer rockstar ownership scrum project crowdfunding seed round creative pitch focus analytics funding [ . . . ]</p>
    <a class="read-more" href="#">READ MORE &nbsp;&gt;</a>
  </article>

  <article class="post">
    <h2 class="post-title">Let the Other 95% of Great Programmers In</h2>
    <p class="post-date">FEBRUARY 10, 2022</p>
    <div class="post-image" role="img" aria-label="Typewriter with a sheet reading funding round" style="background:linear-gradient(180deg,#1a1a1a 0%,#d3d5d6 40%,#56635c 75%,#2e3431 100%)"></div>
    <p class="post-excerpt">The private-equity fund, still in use today, emerged. Private-equity firms organized limited partnerships to hold investments in which the investment professionals served as limited general partner and the investors, limited who were passive limited partners, put up the capital. [ . . . ]</p>
    <a class="read-more" href="#">READ MORE &nbsp;&gt;</a>
  </article>

  <article class="post">
    <h2 class="post-title compact">How To Handle Every Business Growth Challenge With Ease Using These Tips</h2>
    <p class="post-date">FEBRUARY 10, 2022</p>
    <p class="post-excerpt">The private-equity fund, still in use today, emerged. Private-equity firms organized limited partnerships to hold investments in which the investment professionals served as limited general partner and the investors, limited who were passive limited partners, put up the capital. [ . . . ]</p>
    <a class="read-more" href="#">READ MORE &nbsp;&gt;</a>
  </article>
</main>

<aside class="sidebar">
  <h3 class="widget-title">SEARCH</h3>
  <input class="search-input" type="text" aria-label="Search">
  <button class="search-submit">SUBMIT</button>
  <div class="widget-rule"></div>
  <section class="latest">
    <h3 class="widget-title">LATEST POSTS</h3>
    <ul>
      <li>You Will Thank Us - 10 Tips About Capital You Need To Know</li>
      <li>Best Make Capital You Will Read This Year (in 2022)</li>
      <li>10 Secret Things You Didn't Know About Capital</li>
    </ul>
  </section>
</aside>

<a class="pager older" href="#"><svg width="12" height="14" viewBox="0 0 12 14"><path d="M11 1 L1 7 L11 13 Z" fill="#fff"/></svg>OLDER POSTS</a>
<a class="pager newer" href="#">NEWER POSTS<svg width="12" height="14" viewBox="0 0 12 14"><path d="M1 1 L11 7 L1 13 Z" fill="#fff"/></svg></a>

<footer class="site-footer">
  <div class="footer-brand">HOLVENCREST<span class="sub">VENTURES</span></div>
  <nav class="footer-nav">
    <a href="#" style="left:348px">HOME</a>
    <a href="#" style="left:460px">BLOG</a>
    <a href="#" style="left:568px">CONTACT</a>
  </nav>
  <div class="social" style="left:738px" aria-label="Social profile"></div>
  <div class="social" style="left:804px" aria-label="Social profile"></div>
  <div class="footer-rule"></div>
  <p class="copyright">2022 Holvencrest Ventures. All rights reserved.</p>
  <p class="legal"><a href="#">Privacy Policy</a> | <a href="#">Terms Of Service</a></p>
</footer>

</body>
</html>
```